Legal Service Estimated Retainer and Average Case Value

We need an 11x14 flyer that contains the standard retainers and average cost be case, both provided in documents, for each case type we handle. We need the information displayed, preferably in a way that makes the information readable but less troubling to a client shocked at price of litigation. We need one sheet with the retainers and average case value merged into one table.

Target Market(s)

Potential Clients

Font styles to use
Serif
Sans Serif

```html
<!DOCTYPE html>
<html lang="en">
<head>
<meta charset="utf-8">
<title>Retainer and Average Fee Per Case Type</title>
<link href="https://fonts.googleapis.com/css2?family=Cormorant+Garamond:wght@500&family=Roboto:wght@400;500;700&display=swap" rel="stylesheet">
<style>
  :root {
    --navy: #262b57;
    --paper: #f4f4f5;
    --ink: #2c2c33;
    --rule: #3a3a44;
    --backdrop: #dedede;
    --header-wash-a: #ececef;
    --header-wash-b: #d9d9de;
    --photo-a: #c9a98c;
    --photo-b: #8a5a5e;
    --photo-c: #b9b48a;
  }
  * { box-sizing: border-box; margin: 0; padding: 0; }
  html, body { width: 1200px; height: 918px; overflow: hidden; }
  body {
    background: var(--backdrop);
    font-family: "Roboto", Arial, sans-serif;
    color: var(--ink);
    position: relative;
  }
  .flyer {
    position: absolute;
    left: 260px; top: 19px;
    width: 680px; height: 880px;
    background: var(--paper);
    overflow: hidden;
  }
  .header-wash {
    position: absolute; left: 0; top: 0; width: 420px; height: 180px;
    background: linear-gradient(135deg, var(--header-wash-a), var(--header-wash-b));
  }
  .brand {
    position: absolute; left: 34px; top: 72px;
    width: 370px;
    display: flex; align-items: center; gap: 12px;
  }
  .brand-mark { flex: 0 0 40px; width: 40px; height: 40px; background: var(--navy); }
  .brand-name {
    display: flex; flex-direction: column;
    font-family: "Cormorant Garamond", Georgia, serif;
    font-weight: 500; color: var(--navy);
    text-transform: uppercase; line-height: 1;
    white-space: nowrap;
  }
  .brand-prefix { font-size: 13px; letter-spacing: 1px; margin-bottom: 3px; }
  .brand-person { font-size: 24px; letter-spacing: 0.5px; }
  .hero-photo {
    position: absolute; right: 0; top: 0; width: 260px; height: 330px;
    background: linear-gradient(150deg, var(--photo-c) 0%, var(--photo-a) 45%, var(--photo-b) 100%);
  }
  .title-band {
    position: absolute; left: 0; top: 180px; width: 420px; height: 40px;
    background: var(--navy); color: #fff;
    font-weight: 700; font-size: 15px; letter-spacing: 0.3px;
    display: flex; align-items: center; justify-content: center;
    text-transform: uppercase;
  }
  .intro {
    position: absolute; left: 34px; top: 236px; width: 364px;
    font-size: 12.5px; line-height: 1.62; color: var(--ink);
  }
  .fee-table {
    position: absolute; left: 34px; top: 350px; width: 612px;
    border-collapse: collapse; font-size: 12.5px;
  }
  .fee-table th {
    background: var(--navy); color: #fff; font-weight: 700;
    text-transform: uppercase; font-size: 14px; height: 34px;
    letter-spacing: 0.3px; text-align: center;
  }
  .fee-table td {
    height: 30px; border: 1px solid var(--rule);
    padding: 0 10px;
  }
  .fee-table td.case-type { text-align: left; }
  .fee-table .case-type { width: 51%; }
  .fee-table .retainer, .fee-table .avg-fee { text-align: center; white-space: nowrap; }
  .fee-table .retainer { width: 22%; }
  .footer-band {
    position: absolute; left: 0; bottom: 0; width: 100%; height: 92px;
    background: var(--navy); color: #fff;
    display: flex; flex-direction: column; align-items: center; justify-content: center;
    font-weight: 700; font-size: 19px; line-height: 1.35;
  }
</style>
</head>
<body>
  <main class="flyer">
    <div class="header-wash" role="img" aria-label="Faded background photo of a courtroom desk"></div>
    <div class="brand">
      <span class="brand-mark"></span>
      <span class="brand-name">
        <span class="brand-prefix">The Law Office of</span>
        <span class="brand-person">Marcus D Whitfield</span>
      </span>
    </div>
    <div class="hero-photo" role="img" aria-label="Photo of a Lady Justice statue holding scales in front of law books"></div>

    <h1 class="title-band">Retainer and Average Fee Per Case Type</h1>
    <p class="intro">In order for our clients to set expectations for legal fees, we provide the national average range of fees and retainer per case type. These are only to provide you with an understanding of what other cases have cost clients in similar cases. Please note these are not estimates nor guarantees of your own legal costs.</p>

    <table class="fee-table">
      <thead>
        <tr><th class="case-type">Case Type</th><th class="retainer">Retainers</th><th class="avg-fee">Average Fee</th></tr>
      </thead>
      <tbody>
        <tr><td class="case-type">Divorce (3301 C)</td><td class="retainer">$ 2,000</td><td class="avg-fee">$ 1,500 - $ 3,000</td></tr>
        <tr><td class="case-type">Divorce (3301 D)</td><td class="retainer">$ 2,500</td><td class="avg-fee">$ 2,000 - $ 3,000</td></tr>
        <tr><td class="case-type">Divorce &amp; Custody</td><td class="retainer">$ 3,500</td><td class="avg-fee">$ 5,000 - $ 8,000</td></tr>
        <tr><td class="case-type">Divorce &amp; Equitable Distribution</td><td class="retainer">$ 3,500</td><td class="avg-fee">$ 6,000 - $ 10,000</td></tr>
        <tr><td class="case-type">Divorce &amp; Support</td><td class="retainer">$ 3,000</td><td class="avg-fee">$ 2,000 - $ 4,000</td></tr>
        <tr><td class="case-type">Divorce, Custody &amp; Support</td><td class="retainer">$ 3,500</td><td class="avg-fee">$ 8,000 - $ 12,000</td></tr>
        <tr><td class="case-type">Divorce, Equitable Distribution and Support</td><td class="retainer">$ 3,500</td><td class="avg-fee">$ 10,000 - $ 12,000</td></tr>
        <tr><td class="case-type">Divorce, Equitable Distribution and Custody</td><td class="retainer">$ 5,000</td><td class="avg-fee">$ 10,000 - $ 15,000</td></tr>
        <tr><td class="case-type">Divorce, Equitable Distribution, Custody and Support</td><td class="retainer">$ 3,500</td><td class="avg-fee">$ 10,000 - $ 15,000</td></tr>
        <tr><td class="case-type">Custody Initial Order</td><td class="retainer">$ 3,000</td><td class="avg-fee">$ 4,000 - $ 7,000</td></tr>
        <tr><td class="case-type">Custody Modification</td><td class="retainer">$ 3,500</td><td class="avg-fee">$ 5,000 - $ 8,000</td></tr>
        <tr><td class="case-type">Custody and Support</td><td class="retainer">$ 3,000</td><td class="avg-fee">$ 5,000 - $ 8,000</td></tr>
        <tr><td class="case-type">(PFA) Protection From Abuse</td><td class="retainer">$2,000 Paid In Full</td><td class="avg-fee">$ 1,500 - $ 3,000</td></tr>
      </tbody>
    </table>

    <footer class="footer-band">
      <span class="contact-phone">Contact info : (555) 214-0386</span>
      <span class="contact-web">https://www.whitfieldfamilylaw.com</span>
    </footer>
  </main>
</body>
</html>
```